Business card design for new brand

We have recently rebranded and need a new business card template.

We are an insurance underwriting agency. All of our products are sold via other partner companies, so these are just to pass on our details to other organisations.

We would like to see designs that use the colour green (current stationary generally uses lime green (rgb 142,190,63) and forest green (0,154,79) to comply with our logo's colours. We are happy with other shades of green.

Business cards need to include our logo, as well as space for:
1. Full name
2. Qualifications (optional)
3. Title
4. Office number
5. Mobile number
6. Email address

Our logo is enclosed here.

```html
<!DOCTYPE html>
<html lang="en">
<head>
<meta charset="utf-8">
<title>Verdant Cover – Business Card</title>
<link href="https://fonts.googleapis.com/css2?family=Open+Sans:wght@400;600&display=swap" rel="stylesheet">
<style>
  :root {
    --page: #bdb3b3;
    --white: #ffffff;
    --ink: #111111;
    --black: #060606;
    --green: #22dc0e;
    --lime: #86f00a;
    --brand: #1f9e1a;
    --icon: #19b8b0;
  }
  * { margin: 0; padding: 0; box-sizing: border-box; }
  html, body { width: 1200px; height: 960px; overflow: hidden; }
  body {
    background: var(--page);
    font-family: "Open Sans", Arial, sans-serif;
    position: relative;
  }
  .card { position: absolute; overflow: hidden; background: var(--white); }

  /* Front */
  .card-front { left: 253px; top: 46px; width: 678px; height: 388px; }
  .brand {
    position: absolute; left: 0; right: 0; top: 170px;
    display: flex; justify-content: center; align-items: center; gap: 18px;
  }
  .brand-mark { width: 40px; height: 40px; background: var(--green); flex: none; }
  .brand-name { color: var(--ink); font-weight: 600; line-height: 1; }
  .card-front .brand-name .line-1 { display: block; font-size: 50px; letter-spacing: 0.5px; }
  .card-front .brand-name .line-2 { display: block; font-size: 24px; margin-top: 6px; text-align: right; }
  .website {
    position: absolute; left: 0; right: 0; top: 320px;
    text-align: center; font-size: 15px; color: var(--ink);
  }
  .band-lime { position: absolute; left: 0; right: 0; top: 352px; height: 12px; background: var(--lime); }
  .band-green { position: absolute; left: 0; right: 0; top: 364px; height: 24px; background: var(--green); }

  /* Back */
  .card-back { left: 254px; top: 506px; width: 672px; height: 383px; }
  .stripe-green { position: absolute; left: 0; top: 0; width: 31px; height: 100%; background: var(--green); }
  .stripe-lime { position: absolute; left: 31px; top: 0; width: 15px; height: 100%; background: var(--lime); }
  .card-back .brand { left: 46px; right: auto; width: 282px; top: 188px; gap: 10px; }
  .card-back .brand-mark { width: 24px; height: 24px; }
  .card-back .brand-name .line-1 { display: block; font-size: 27px; }
  .card-back .brand-name .line-2 { display: block; font-size: 13px; margin-top: 3px; text-align: right; }

  .info-panel { position: absolute; left: 328px; top: 0; width: 344px; height: 100%; background: var(--black); }
  .name-accent { position: absolute; left: 0; top: 98px; width: 4px; height: 46px; background: var(--green); }
  .person-name {
    position: absolute; left: 20px; top: 96px;
    color: var(--white); font-weight: 600; font-size: 24px; letter-spacing: 0.5px;
  }
  .person-name .qualification { font-weight: 400; font-size: 17px; margin-left: 6px; }
  .person-title { position: absolute; left: 20px; top: 127px; color: var(--green); font-size: 15px; }
  .title-rule { position: absolute; left: 111px; right: 0; top: 136px; height: 2px; background: var(--green); }

  .contact {
    position: absolute; left: -4px; width: 348px; height: 28px;
    background: var(--green); display: flex; align-items: center;
  }
  .contact::after {
    content: ""; position: absolute; right: 0; top: 0; width: 14px; height: 100%; background: var(--lime);
  }
  .contact-phone { top: 228px; }
  .contact-mobile { top: 273px; }
  .contact-email { top: 322px; }
  .contact-icon {
    width: 26px; height: 26px; border-radius: 50%; background: var(--white);
    margin-left: 20px; display: flex; align-items: center; justify-content: center;
    color: var(--icon); font-weight: 600; font-size: 16px; flex: none;
  }
  .contact-text { margin-left: 12px; color: var(--white); font-size: 16px; }
</style>
</head>
<body>

<section class="card card-front">
  <div class="brand">
    <span class="brand-mark"></span>
    <span class="brand-name"><span class="line-1">Verdant Cover</span><span class="line-2">Pty Ltd</span></span>
  </div>
  <p class="website">www.verdantcover.com</p>
  <div class="band-lime"></div>
  <div class="band-green"></div>
</section>

<section class="card card-back">
  <div class="stripe-green"></div>
  <div class="stripe-lime"></div>
  <div class="brand">
    <span class="brand-mark"></span>
    <span class="brand-name"><span class="line-1">Verdant Cover</span><span class="line-2">Pty Ltd</span></span>
  </div>

  <div class="info-panel">
    <div class="name-accent"></div>
    <h1 class="person-name">MARLO KEANE<span class="qualification">MBA</span></h1>
    <p class="person-title">Chief Officer</p>
    <div class="title-rule"></div>

    <div class="contact contact-phone">
      <span class="contact-icon">
        <svg width="14" height="14" viewBox="0 0 24 24"><path fill="var(--icon)" d="M6.6 10.8a15.1 15.1 0 0 0 6.6 6.6l2.2-2.2c.3-.3.7-.4 1-.2 1.1.4 2.3.6 3.6.6.6 0 1 .4 1 1V20c0 .6-.4 1-1 1C10.6 21 3 13.4 3 4c0-.6.4-1 1-1h3.5c.6 0 1 .4 1 1 0 1.3.2 2.5.6 3.6.1.3 0 .7-.2 1z"/></svg>
      </span>
      <span class="contact-text">732-555-0142</span>
    </div>
    <div class="contact contact-mobile">
      <span class="contact-icon">
        <svg width="12" height="16" viewBox="0 0 12 16"><rect x="1.5" y="1" width="9" height="14" rx="1.5" fill="none" stroke="var(--icon)" stroke-width="1.5"/><circle cx="6" cy="12.5" r="0.9" fill="var(--icon)"/></svg>
      </span>
      <span class="contact-text">732-555-0187</span>
    </div>
    <div class="contact contact-email">
      <span class="contact-icon">@</span>
      <span class="contact-text">email@verdantcover.com</span>
    </div>
  </div>
</section>

</body>
</html>
```